New professional looking flyer for company

I need our flyer updated my flyer is the Lvb flyer Have attached current flyer so you know what services need to be listed. Want it to be in mainly dark colours like black and dark grey with pops of light grey, silver or white. i have added several photos for you to choose which ones work best with your design would like The photos to be in colour for the flyer. But can have a mix of greyscale if that works for your design j have attached another companies flyers as design ideas to show what I am looking for

Target Market(s)

new clients

Industry/Entity Type

transport and earthmoving

Colors

Designer to choose colors to be used in the design.

Requirements
Nice to have
• Look professional
Should not have
• No orange or red or green

```html
<!DOCTYPE html>
<html lang="en">
<head>
<meta charset="utf-8">
<title>Lvb Pty Ltd – Our Service Flyer</title>
<link rel="stylesheet" href="https://fonts.googleapis.com/css2?family=Barlow+Condensed:wght@400;500;600;700;800&display=swap">
<style>
  :root {
    --page-bg: #e4e4e4;
    --flyer-bg: #141414;
    --flyer-bg-soft: #262626;
    --silver: #d6d6d6;
    --silver-dark: #a8a8a8;
    --text-light: #e6e6e6;
    --text-muted: #b4b4b4;
    --white: #ffffff;
  }
  * { box-sizing: border-box; margin: 0; padding: 0; }
  html, body {
    width: 1200px; height: 1163px; overflow: hidden;
    background: var(--page-bg);
    font-family: "Barlow Condensed", sans-serif;
  }
  .flyer {
    position: absolute; left: 215px; top: 30px;
    width: 770px; height: 1103px; overflow: hidden;
    background: radial-gradient(ellipse at 40% 30%, var(--flyer-bg-soft), var(--flyer-bg) 70%);
    box-shadow: 0 14px 40px rgba(0,0,0,.35);
  }
  .flyer__bands { position: absolute; inset: 0; }
  .photo { position: absolute; }
  .photo--hero {
    left: 0; top: 57px; width: 640px; height: 445px;
    background: linear-gradient(135deg, #6b6b6b 0%, #cfcfcf 45%, #8d8d8d 70%, #3d3d3d 100%);
    clip-path: polygon(0 0, 470px 0, 470px 130px, 100% 130px, 100% 100%, 0 100%);
  }
  .photo--truck-dark {
    left: 377px; top: 842px; width: 393px; height: 261px;
    background: linear-gradient(160deg, #3a3a3a 0%, #0c0c0c 60%, #454545 100%);
    clip-path: polygon(0 100px, 210px 45px, 393px 0, 100% 100%, 0 100%);
  }
  .brand {
    position: absolute; left: 491px; top: 42px; width: 268px; height: 135px;
    text-align: center; color: var(--silver); z-index: 2;
  }
  .brand__rule { height: 3px; background: var(--silver); }
  .brand__name { font-weight: 800; font-size: 92px; line-height: 96px; letter-spacing: 4px; }
  .brand__suffix { font-weight: 800; font-size: 22px; line-height: 26px; margin-bottom: 6px; }
  .tilted { position: absolute; transform-origin: 0 0; transform: rotate(-16deg); z-index: 2; }
  .headline {
    left: 44px; top: 626px;
    font-weight: 800; font-size: 76px; line-height: 1; letter-spacing: 1px;
    color: var(--silver);
    text-shadow: 0 3px 0 #7a7a7a, 0 5px 8px rgba(0,0,0,.6);
  }
  .service-list { list-style: none; color: var(--text-light); font-size: 21px; font-weight: 500; line-height: 28px; }
  .service-list li::before {
    content: ""; display: inline-block; width: 10px; height: 10px; border-radius: 50%;
    background: var(--white); margin-right: 6px; vertical-align: 1px;
  }
  .service-list--left { left: 46px; top: 734px; }
  .service-list--right { left: 356px; top: 638px; }
  .tagline { left: 356px; top: 842px; color: var(--text-light); }
  .tagline__intro { font-size: 20px; font-weight: 400; line-height: 26px; }
  .tagline__call { font-size: 21px; font-weight: 700; line-height: 24px; text-transform: uppercase; color: var(--white); }
  .contact { position: absolute; left: 42px; top: 955px; width: 302px; z-index: 2; }
  .contact__phone {
    display: flex; align-items: center; gap: 10px;
    font-weight: 700; font-size: 48px; color: var(--silver); line-height: 1;
    padding-bottom: 10px; border-bottom: 1.5px solid var(--silver-dark);
  }
  .contact__icon { width: 38px; height: 38px; flex: none; }
  .contact__company { margin-top: 10px; font-weight: 700; font-size: 17px; color: var(--text-light); }
  .contact__line { font-size: 15px; color: var(--text-muted); line-height: 20px; }
</style>
</head>
<body>
<main class="flyer">
  <svg class="flyer__bands" width="770" height="1103" viewBox="0 0 770 1103" aria-hidden="true">
    <defs>
      <linearGradient id="bandFade" x1="0" x2="1">
        <stop offset="0" stop-color="#6a6a6a" stop-opacity=".9"/>
        <stop offset="1" stop-color="#2a2a2a" stop-opacity=".5"/>
      </linearGradient>
      <linearGradient id="bandTag" x1="0" x2="1">
        <stop offset="0" stop-color="#3a3a3a" stop-opacity="0"/>
        <stop offset="1" stop-color="#6a6a6a" stop-opacity=".8"/>
      </linearGradient>
    </defs>
    <polygon points="0,655 770,434 770,484 0,705" fill="url(#bandFade)"/>
    <polygon points="0,320 770,100 770,150 0,370" fill="#1e1e1e"/>
    <polygon points="200,905 770,742 770,790 200,953" fill="url(#bandTag)"/>
  </svg>

  <div class="photo photo--hero" role="img" aria-label="Photo of a white prime mover hauling an oversize earthmoving machine on a low loader"></div>
  <div class="photo photo--truck-dark" role="img" aria-label="Photo of a black road train prime mover with a bull bar"></div>

  <div class="brand">
    <div class="brand__rule"></div>
    <div class="brand__name">Lvb</div>
    <div class="brand__suffix">Pty Ltd</div>
    <div class="brand__rule"></div>
  </div>

  <h1 class="tilted headline">OUR SERVICE</h1>

  <ul class="tilted service-list service-list--left">
    <li>Over size loads / Hot Shot Loads</li>
    <li>Heavy Vehicle Recovery Services</li>
    <li>Potable Water Deliveries</li>
    <li>Road Building / Maintenance</li>
    <li>Earthworks</li>
    <li>Sand &amp; Metal Supply &amp; Cartage</li>
  </ul>

  <ul class="tilted service-list service-list--right">
    <li>Road Train Train Tippers</li>
    <li>Road Train Tankers</li>
    <li>Road Train Flat Tops</li>
    <li>Drop Deck Trailers</li>
    <li>Mine Site accredited equipment &amp; Operators</li>
    <li>Traffic Management</li>
  </ul>

  <div class="tilted tagline">
    <p class="tagline__intro">We offer a large range of services not listed so</p>
    <p class="tagline__call">Call us today for a personalised<br>quote to suit your needs.</p>
  </div>

  <div class="contact">
    <div class="contact__phone">
      <svg class="contact__icon" viewBox="0 0 40 40" aria-hidden="true">
        <circle cx="20" cy="20" r="19" fill="#d6d6d6"/>
        <path d="M14 10c1 0 2 2.5 2.6 4 .3.8-.4 1.6-1.2 2.3 1 2.6 3.4 5 6 6 .7-.8 1.5-1.5 2.3-1.2 1.5.6 4 1.6 4 2.6 0 1.6-2 4-4.2 4C16.5 27.7 12 23 12 14.3 12 12 12.6 10 14 10z" fill="#141414"/>
      </svg>
      041 555 2790
    </div>
    <p class="contact__company">Lvb Pty Ltd</p>
    <p class="contact__line">Depot: Lot 52, Ridge Track Road Redstone</p>
    <p class="contact__line">accounts@lvbhaulage.com.au</p>
  </div>
</main>
</body>
</html>
```